Urkundendesign für Jahrgangsbeste einer Realschule gesucht
Der Elternbeirat der Realschule Lindwerth benötigt für die Jahrgangsbesten des Abschlussjahrgangs eine Urkunde. Gerne mit Prägung (was kostet sowas bei Druck?!?). Das von-Halmberg-Logo darf benutzt werden (siehe Homepage).
es soll eine Urkunde für den/die 'Jahrgangsbeste 2026' geben. das Datum, sowie SchülerInnen-Name würden wir jeweils handschriftlich anbringen.
die Urkunde in A4 gestalten.
wir benötigen die üblichen druckbaren Dateien, sodass eine Druckerei dann auch selbst Jahr für Jahr das Jahr abändern kann.
bitte um Vorschläge, wir arbeiten uns nach und nach da durch.
nicht zu viel Schnörkelei.

```html
<!DOCTYPE html>
<html lang="de">
<head>
<meta charset="utf-8">
<title>Urkunde Jahrgangsbeste 2026 – Realschule Lindwerth</title>
<link rel="stylesheet" href="https://fonts.googleapis.com/css2?family=Marcellus&family=Playfair+Display:wght@800&family=Cinzel:wght@700&family=Pinyon+Script&family=Figtree:wght@400;600&display=swap">
<style>
  :root {
    --page-bg: #d6d6d6;
    --paper: #ffffff;
    --teal: #1fae9c;
    --teal-light: #5ccac0;
    --teal-dark: #0e9483;
    --green: #5cb85c;
    --green-dark: #449a45;
    --yellow: #f7c41a;
    --ink: #1c1c1c;
  }
  * { margin: 0; padding: 0; box-sizing: border-box; }
  html, body {
    width: 923px; height: 1200px; overflow: hidden;
    background: var(--page-bg);
  }
  .certificate {
    position: absolute;
    left: 21.5px; top: 289px;
    width: 880px; height: 622px;
    background: var(--paper);
    overflow: hidden;
    box-shadow: 0 14px 34px rgba(0,0,0,.28);
  }
  .decor {
    position: absolute; inset: 0; width: 100%; height: 100%;
  }
  .centered {
    position: absolute; left: 0; width: 100%; text-align: center;
  }
  .title-kicker {
    top: 68px;
    font-family: "Marcellus", serif;
    font-size: 33px; line-height: 1; letter-spacing: .5px;
    color: var(--teal);
  }
  .title-main {
    top: 96px;
    font-family: "Playfair Display", serif;
    font-weight: 800; font-size: 56px; line-height: 1.05;
    font-variant-numeric: lining-nums;
    color: var(--green);
  }
  .presented-to {
    top: 166px;
    font-family: "Cinzel", serif;
    font-weight: 700; font-size: 15px; letter-spacing: .2px;
    color: var(--ink);
  }
  .recipient {
    top: 196px;
    font-family: "Pinyon Script", cursive;
    font-size: 86px; line-height: 1;
    color: var(--teal);
  }
  .recipient-line {
    position: absolute; left: 153px; width: 575px; top: 292px;
    border-top: 1.5px solid var(--green);
  }
  .body-text {
    top: 308px; left: 150px; width: 580px;
    font-family: "Figtree", sans-serif;
    font-size: 14.6px; line-height: 18.7px;
    color: var(--ink);
  }
  .school-mark {
    position: absolute; left: 96px; top: 430px;
    display: flex; align-items: center; gap: 6px;
    font-family: "Figtree", sans-serif;
    font-weight: 600; font-size: 15px;
    color: var(--green-dark);
  }
  .school-mark__dot {
    width: 12px; height: 12px; border-radius: 50%;
    background: var(--green-dark);
  }
  .signature {
    position: absolute; top: 443px; width: 202px;
    border-top: 1.2px solid var(--ink);
    padding-top: 8px;
    text-align: center;
    font-family: "Figtree", sans-serif;
    font-weight: 600; font-size: 15px;
    color: var(--ink);
  }
  .signature--name { left: 239px; }
  .signature--date { left: 470px; }
</style>
</head>
<body>
<main class="certificate">
  <svg class="decor" viewBox="0 0 880 622" preserveAspectRatio="none" role="img" aria-label="Farbflächen in Türkis, Grün und Gelb als Randgestaltung">
    <defs>
      <linearGradient id="tealSoft" x1="0" y1="0" x2="0" y2="1">
        <stop offset="0" stop-color="#5ccac0"/>
        <stop offset="1" stop-color="#0e9483"/>
      </linearGradient>
      <linearGradient id="groundSoft" x1="0" y1="0" x2="1" y2="0">
        <stop offset="0" stop-color="#5cb85c"/>
        <stop offset="1" stop-color="#f7c41a"/>
      </linearGradient>
    </defs>
    <path d="M0 0 H165 C85 40 30 110 0 182 Z" fill="url(#tealSoft)"/>
    <path d="M880 254 C850 380 760 480 625 515 L880 515 Z" fill="url(#tealSoft)"/>
    <path d="M0 493 C300 560 620 560 880 515 V622 H0 Z" fill="url(#groundSoft)"/>
  </svg>

  <p class="centered title-kicker">URKUNDE FÜR DEN/DIE</p>
  <h1 class="centered title-main">JAHRGANGSBESTE 2026</h1>
  <p class="centered presented-to">Dieses Zertifikat wird mit Stolz überreicht an</p>
  <p class="centered recipient">Lorem Ipsum</p>
  <div class="recipient-line"></div>
  <p class="centered body-text">Lorem ipsum dolor sit amet, consectetur adipiscing elit, sed do eiusmod tempor incididunt ut labore et dolore magna aliqua. Ut enim ad minim veniam, quis nostrud exercitation ullamco laboris nisi ut aliquip ex ea commodo consequat.</p>

  <div class="school-mark">
    <span class="school-mark__dot"></span>
    <span class="school-mark__name">von-Halmberg</span>
  </div>

  <div class="signature signature--name">Unterschrift</div>
  <div class="signature signature--date">Datum</div>
</main>
</body>
</html>
```